BrovaLT BIZ Card, email signature & Stationary

Professional business cards, email signatures and ms word letterhead

Target Market(s)

business owners

Industry/Entity Type

cloud hosting

Contact Information for Business Card

name title office phone number , direct line, fax email address web site

Font styles to use
Other font styles liked:
• something that compliments font in logo

```html
<!DOCTYPE html>
<html lang="en">
<head>
<meta charset="utf-8">
<title>BrovaLT Business Card</title>
<link href="https://fonts.googleapis.com/css2?family=Jost:wght@300;400;500&display=swap" rel="stylesheet">
<style>
  :root {
    --backdrop: #5b5b5b;
    --card-white: #ffffff;
    --card-black: #000000;
    --brand-red: #e8323a;
    --ink: #000000;
    --text-grey: #5a5a5a;
  }
  html, body {
    margin: 0;
    padding: 0;
    width: 1200px;
    height: 1200px;
    overflow: hidden;
    background: var(--backdrop);
    font-family: 'Jost', sans-serif;
  }
  .canvas {
    position: relative;
    width: 1200px;
    height: 1200px;
  }
  .card {
    position: absolute;
    left: 263px;
    width: 690px;
    height: 394px;
    box-sizing: border-box;
  }
  .card--front {
    top: 158px;
    background: var(--card-white);
  }
  .card--back {
    top: 651px;
    left: 260px;
    width: 692px;
    background: var(--card-black);
    display: flex;
    align-items: center;
    justify-content: center;
  }
  .contact-block {
    position: absolute;
    left: 42px;
    top: 180px;
    width: 170px;
  }
  .person-name {
    margin: 0;
    font-size: 23px;
    font-weight: 400;
    color: var(--brand-red);
    letter-spacing: -0.4px;
    line-height: 1;
    white-space: nowrap;
  }
  .person-title {
    margin: 9px 0 0;
    font-size: 15px;
    font-weight: 400;
    color: var(--text-grey);
    line-height: 1;
  }
  .contact-list {
    list-style: none;
    margin: 22px 0 0;
    padding: 0;
  }
  .contact-item {
    display: flex;
    align-items: center;
    height: 20.6px;
    font-size: 17px;
    color: var(--text-grey);
    line-height: 1;
    white-space: nowrap;
  }
  .contact-icon {
    width: 14px;
    height: 14px;
    margin-right: 14px;
    flex: none;
    fill: var(--brand-red);
  }
  .brand-mark {
    position: absolute;
    left: 232px;
    top: 130px;
    display: flex;
    align-items: center;
  }
  .brand-square {
    width: 30px;
    height: 30px;
    background: var(--brand-red);
    margin-right: 14px;
    flex: none;
  }
  .brand-name {
    font-size: 112px;
    font-weight: 500;
    color: var(--ink);
    line-height: 1;
    letter-spacing: -1px;
    white-space: nowrap;
  }
  .brand-name--reverse {
    font-size: 130px;
    font-weight: 300;
    color: var(--brand-red);
    letter-spacing: -1px;
    line-height: 1;
    white-space: nowrap;
  }
</style>
</head>
<body>
<main class="canvas">
  <section class="card card--front">
    <div class="contact-block">
      <h1 class="person-name">DANA MERROW</h1>
      <p class="person-title">President</p>
      <ul class="contact-list">
        <li class="contact-item">
          <svg class="contact-icon" viewBox="0 0 16 16" aria-hidden="true"><path d="M3.5 1.2l2.4 2.6-1.3 1.8c.9 2 2.6 3.7 4.6 4.6l1.8-1.3 2.6 2.4-1.5 2.4C6.8 13.4 2.6 9.2 1.1 2.7z"/></svg>
          555-210-4831
        </li>
        <li class="contact-item">
          <svg class="contact-icon" viewBox="0 0 16 16" aria-hidden="true"><path d="M4 0h8a1 1 0 0 1 1 1v14a1 1 0 0 1-1 1H4a1 1 0 0 1-1-1V1a1 1 0 0 1 1-1zm.8 1.6v11h6.4v-11zM8 13.4a.8.8 0 1 0 0 1.6.8.8 0 0 0 0-1.6z"/></svg>
          555-210-4872
        </li>
        <li class="contact-item">
          <svg class="contact-icon" viewBox="0 0 16 16" aria-hidden="true"><path d="M4 1h7l1 1v4H4zM1 7h14v6H1zm3 4h8v4H4z"/></svg>
          555-210-4890
        </li>
        <li class="contact-item">
          <svg class="contact-icon" viewBox="0 0 16 16" aria-hidden="true"><path d="M1 3h14v10H1zm1.5 1.5v.4L8 9l5.5-4.1v-.4zm0 2.2v4.8h11V6.7L8 10.8z"/></svg>
          info@BrovaLT.com
        </li>
        <li class="contact-item">
          <svg class="contact-icon" viewBox="0 0 16 16" aria-hidden="true"><circle cx="8" cy="8" r="7.5"/></svg>
          www.BrovaLT.com
        </li>
      </ul>
    </div>
    <div class="brand-mark">
      <span class="brand-square"></span>
      <span class="brand-name">BrovaLT</span>
    </div>
  </section>

  <section class="card card--back">
    <span class="brand-name--reverse">BrovaLT</span>
  </section>
</main>
</body>
</html>
```